Bramble Harbor Foundation Web Design

The design we need is for a WordPress blog that will be our content platform. We are a registered 501(c)3 non-profit that focuses on financially supporting the treatment of cancer patients that have been told they have no hope and there is nothing the conventional medical system can do for them. Through this wesbite we want to both rasie awareness about the treatment options plus, raise funds for treating patients. The two primary target audiences of the site are...

1. Terminally ill patients and their families to let them know that there is an option other then hospice and that we are hear to support that option.

2. People looking to help donate to a worthwhile cause that resonates with them.

The website is https://brambleharborfoundation.org/

See attached logo designs!!!

Target Market(s)

Cancer patients and their families

Industry/Entity Type

Foundation

Font styles to use
Sans Serif

Colors
ffffff
fbed22

Requirements
Must have
• I like this look of this site. It is clean, simple, helpful, soft. I like the flow of the pages.
• http://www.quietmeadowtrust.org/
• I like the design and flow but NOT the color or boldness
• https://tmvq-youth.org/
• I like this style for a donation page.
• https://www.curewaveaid.org/about-cwa/stand-with-us/gifts/single-gift
• with the addition of a Would you like your employer to match? button.
Nice to have
• White black and gold - but soft
• Even possibly grayscale like the site I like.

```html
<!DOCTYPE html>
<html lang="en">
<head>
<meta charset="utf-8">
<title>Bramble Harbor Foundation</title>
<link rel="stylesheet" href="https://fonts.googleapis.com/css2?family=Mulish:wght@400;500;600;700;800&family=Open+Sans:wght@400;500&display=swap">
<style>
  :root {
    --page-bg: #f4f4f4;
    --nav-bg: #2b2b2b;
    --yellow: #fbed22;
    --gold: #e8c34a;
    --ink: #222222;
    --muted: #555b60;
    --mist: #dadfe2;
    --green: #2e962e;
    --white: #ffffff;
  }
  * { margin: 0; padding: 0; box-sizing: border-box; }
  html, body { width: 1200px; height: 1200px; overflow: hidden; }
  body { background: var(--page-bg); font-family: "Mulish", sans-serif; color: var(--ink); position: relative; }

  .site-header { position: absolute; left: 0; top: 0; width: 1200px; height: 83px; background: var(--page-bg); }
  .brand { position: absolute; left: 162px; top: 24px; display: flex; align-items: center; gap: 8px; }
  .brand-dot { width: 22px; height: 22px; border-radius: 50%; background: var(--gold); }
  .brand-name { font-size: 15px; font-weight: 700; color: var(--ink); letter-spacing: 0.3px; }
  .donate-btn { position: absolute; left: 896px; top: 22px; width: 144px; height: 40px; background: var(--yellow); border-radius: 3px; display: flex; align-items: center; justify-content: center; font-size: 12px; font-weight: 500; letter-spacing: 0.5px; box-shadow: 0 1px 3px rgba(0,0,0,0.15); }

  .main-nav { position: absolute; left: 0; top: 83px; width: 1200px; height: 48px; background: var(--nav-bg); }
  .nav-item { position: absolute; top: 17px; color: #e8e8e8; font-size: 11px; font-weight: 500; letter-spacing: 0.4px; white-space: nowrap; }
  .nav-item.is-active { color: var(--white); font-weight: 800; }
  .nav-underline { position: absolute; left: 333px; top: 45px; width: 144px; height: 3px; background: var(--yellow); }

  .hero { position: absolute; left: 0; top: 131px; width: 1200px; height: 400px; background: linear-gradient(100deg, #5a5e60 0%, #6b6e6f 35%, #8a7466 60%, #4f5f6a 85%, #5e7489 100%); }
  .hero-title { position: absolute; left: 161px; top: 244px; font-size: 38px; font-weight: 700; color: var(--white); letter-spacing: 1px; }
  .hero-text { position: absolute; left: 161px; top: 300px; width: 320px; font-size: 10.5px; line-height: 13.5px; color: var(--white); }
  .hero-btn { position: absolute; left: 161px; top: 367px; width: 148px; height: 44px; border: 2px solid var(--yellow); border-radius: 4px; display: flex; align-items: center; justify-content: center; color: var(--white); font-size: 11.5px; font-weight: 500; }

  .scroll-cue { position: absolute; left: 580px; top: 511px; width: 40px; height: 40px; border-radius: 50%; background: var(--yellow); display: flex; align-items: center; justify-content: center; z-index: 3; }

  .mission { position: absolute; left: 0; top: 531px; width: 1200px; height: 463px; background: var(--mist); }
  .road-photo { position: absolute; left: 161px; top: 514px; width: 300px; height: 496px; background: linear-gradient(180deg, #3f78c4 0%, #9ab7dc 25%, #6e86b4 45%, #8594b8 70%, #7d8bae 100%); border-bottom: 4px solid var(--yellow); box-shadow: 0 2px 6px rgba(0,0,0,0.2); z-index: 2; }
  .motto { position: absolute; left: 0; top: 592px; width: 624px; text-align: center; font-size: 72px; font-weight: 800; line-height: 80px; color: var(--white); z-index: 3; letter-spacing: -0.5px; }
  .motto-text { position: absolute; left: 102px; top: 795px; width: 420px; text-align: center; font-size: 13.5px; line-height: 17.5px; color: #333; z-index: 3; }

  .info-col { position: absolute; left: 630px; width: 380px; text-align: center; }
  .info-title { font-size: 18px; font-weight: 500; letter-spacing: 0.3px; color: var(--ink); }
  .info-text { margin-top: 14px; font-size: 10.5px; line-height: 13.6px; color: var(--muted); }
  .learn-btn { position: absolute; left: 740px; top: 850px; width: 160px; height: 40px; background: var(--green); border-radius: 2px; color: var(--white); font-size: 11.5px; font-weight: 600; display: flex; align-items: center; justify-content: center; gap: 12px; }

  .section-title { position: absolute; left: 0; top: 1044px; width: 1200px; text-align: center; font-family: "Open Sans", sans-serif; font-size: 37px; color: var(--ink); }
  .card-photo { position: absolute; top: 1120px; width: 264px; height: 80px; }
</style>
</head>
<body>
  <header class="site-header">
    <div class="brand"><span class="brand-dot"></span><span class="brand-name">Bramble Harbor Foundation</span></div>
    <div class="donate-btn">DONATE</div>
  </header>

  <nav class="main-nav">
    <span class="nav-item" style="left:161px">CANCER INFORMATION</span>
    <span class="nav-item is-active" style="left:335px">TREATMENTS &amp; SUPPORT</span>
    <span class="nav-item" style="left:534px">SURVIVOR&nbsp; STORIES</span>
    <span class="nav-item" style="left:691px">RESEARCH</span>
    <span class="nav-item" style="left:798px">NEWS &amp; EVENTS</span>
    <span class="nav-item" style="left:936px">ABOUT US</span>
    <span class="nav-underline"></span>
  </nav>

  <section class="hero" role="img" aria-label="Group of people stacking their hands together in unity">
    <h1 class="hero-title" style="top:113px">Let's Beat Cancer!</h1>
    <p class="hero-text" style="top:176px">One day everyone will beat cancer, the more research we do, the sooner that day will come. Ipsum dolor sit amet, consectetur adipiscing elit. Ut ut nulla vel velit pulvinar lobortis.</p>
    <div class="hero-btn" style="top:236px">GET INVOLVED</div>
  </section>

  <div class="scroll-cue">
    <svg width="20" height="12" viewBox="0 0 20 12"><path d="M1 1 L10 10 L19 1" fill="none" stroke="#222" stroke-width="1.8"/></svg>
  </div>

  <section class="mission"></section>
  <div class="road-photo" role="img" aria-label="Long road across a bridge under a blue sky"></div>
  <h2 class="motto">Never give up,<br>Never give in.</h2>
  <p class="motto-text">Neque porro quisquam est qui dolorem ipsum quia dolor sit amet, consectetur, adipisci velit. In tincidunt lectus nec felis ornare, at rutrum odio cursus. Donec in metus quis eros aliquet maxim et eget nisi. Interdum et malesuadafames ac ante ipsum.</p>

  <div class="info-col" style="top:630px">
    <h3 class="info-title">OUR PURPOSE</h3>
    <p class="info-text">Sed maximus lacinia lectus, eu tincidunt lacus maximus posuere. Maecenas sagittis tristique placerat. Maecenas ac odio rutrum, convallis purus id, commodo lectus. Nam semper augue laoreet, sodales sem at, euismod nisi.</p>
  </div>
  <div class="info-col" style="top:743px">
    <h3 class="info-title">OUR PROGRESS</h3>
    <p class="info-text">Sed maximus lacinia lectus, eu tincidunt lacus maximus posuere. Maecenas sagittis tristique placerat. Maecenas ac odio rutrum, convallis purus id, commodo lectus. Nam semper augue laoreet, sodales sem at, euismod nisi.</p>
  </div>
  <div class="learn-btn">LEARN MORE
    <svg width="6" height="10" viewBox="0 0 6 10"><path d="M1 1 L5 5 L1 9" fill="none" stroke="#fff" stroke-width="1.2"/></svg>
  </div>

  <h2 class="section-title">Treatments &amp; Support</h2>
  <div class="card-photo" role="img" aria-label="Hospital treatment room with medical monitors" style="left:160px;background:linear-gradient(135deg,#1c3a6e,#2f7fd6 60%,#8fd0f5)"></div>
  <div class="card-photo" role="img" aria-label="Bright clinic hallway" style="left:468px;background:linear-gradient(180deg,#e8e8e8,#b9bcbc)"></div>
  <div class="card-photo" role="img" aria-label="Medical team joining hands" style="left:776px;background:linear-gradient(135deg,#f2efec,#e8b37a 60%,#f4eee8)"></div>
</body>
</html>
```